My Book needs a front and back cover design

I need you to design my front and back cover of my book. The title of my book is : Beyond the Silent Pause
My Story
5 steps to speaking fluently forever

The picture that I uploaded needs to be on the front cover. On the back cover it should be excerpt from Chapter One like this :

As years have gone by I have become much more conscious about my problem with stuttering, more able to relax my muscles to alleviate it. At the age of 20, I realized that stuttering is like a demon in my head that needs to be killed and that nothing is wrong with me. Furthermore, no one can help me but myself. I'm holding the key of my future. Everything is just in my head.

With this book, I want to help you realize that nobody can help you fix your stuttering better than yourself. There's no quick-get-rid-of-stuttering cure. The cure lies inside of you.

- Lukas Orbeck, excerpt from Chapter One
----------------------------------------------------------------------------------

My name also needs to be located on the front cover.

Target Market(s)

80 million people who stutter each day

Industry/Entity Type

Psychology

Font styles to use
Serif
Sans Serif

Colors
1b1b1b
000000
333333

Requirements
Must have
• Front Cover : Full Title and subtitle and my name and my picture
• Back Cover : Excerpt from my Chapter One with my name below just as I have described in my project description
Nice to have
• Maybe black background would be the best for the front cover.

```html
<!DOCTYPE html>
<html lang="en">
<head>
<meta charset="utf-8">
<title>Beyond the Silent Pause — Book Cover</title>
<link rel="stylesheet" href="https://fonts.googleapis.com/css2?family=Crimson+Text:ital,wght@0,400;0,700;1,400&family=Libre+Baskerville:wght@400;700&family=Roboto:wght@700;900&display=swap">
<style>
  :root {
    --gold: #d7b034;
    --gold-light: #e2bd45;
    --charcoal: #333333;
    --ink: #1b1b1b;
    --line: #3a3a3a;
    --white: #ffffff;
    --rule: #9a9a9a;
  }
  * { margin: 0; padding: 0; box-sizing: border-box; }
  html, body { width: 1200px; height: 900px; overflow: hidden; background: var(--charcoal); }
  .cover { position: relative; width: 1200px; height: 900px; overflow: hidden; }

  /* Back cover */
  .back-cover { position: absolute; left: 0; top: 0; width: 580px; height: 900px; background: var(--gold); }
  .excerpt-box {
    position: absolute; left: 47px; top: 35px; width: 490px; height: 462px;
    border: 2.5px solid var(--line); border-radius: 16px; padding: 14px 20px 0 21px;
  }
  .excerpt-text {
    font-family: "Crimson Text", serif; font-style: italic; font-size: 21.5px;
    line-height: 29.6px; color: var(--ink);
  }
  .excerpt-text + .excerpt-text { margin-top: 6px; }
  .excerpt-credit {
    font-family: "Crimson Text", serif; font-weight: 700; font-size: 21px;
    color: var(--ink); margin-top: 8px; padding-left: 15px;
  }
  .about-box {
    position: absolute; left: 47px; top: 512px; width: 490px; height: 209px;
    border: 2.5px solid var(--line); border-radius: 16px;
  }
  .about-title {
    font-family: "Crimson Text", serif; font-weight: 700; font-size: 22px;
    letter-spacing: 0.5px; text-align: center; color: var(--ink); margin-top: 16px;
  }
  .isbn-box {
    position: absolute; left: 323px; top: 736px; width: 213px; height: 128px;
    border: 1.5px solid #111;
  }
  .isbn-label {
    font-family: "Crimson Text", serif; font-size: 15px; font-variant: small-caps;
    text-align: center; color: var(--ink); margin-top: 1px;
  }

  /* Spine */
  .spine { position: absolute; left: 580px; top: 0; width: 40px; height: 900px; background: var(--charcoal); border-right: 1px solid #555; }
  .spine-title, .spine-author {
    position: absolute; left: 50%; transform: translateX(-50%);
    writing-mode: vertical-rl; color: var(--gold); white-space: nowrap;
  }
  .spine-title { top: 66px; font-family: "Libre Baskerville", serif; font-size: 15px; letter-spacing: 1.5px; }
  .spine-author { top: 728px; font-family: "Roboto", sans-serif; font-weight: 700; font-size: 13.5px; letter-spacing: 0.5px; }

  /* Front cover */
  .front-cover { position: absolute; left: 621px; top: 0; width: 579px; height: 900px; background: var(--charcoal); }
  .book-title {
    position: absolute; left: 0; top: 28px; width: 100%; text-align: center;
    font-family: "Libre Baskerville", serif; font-weight: 700; font-size: 52px;
    line-height: 70px; letter-spacing: 1.5px; color: var(--gold);
    -webkit-text-stroke: 1.5px var(--white); paint-order: stroke fill;
  }
  .book-subtitle {
    position: absolute; left: 0; top: 178px; width: 100%; text-align: center;
    font-family: "Roboto", sans-serif; font-weight: 700; font-size: 33px; color: var(--gold);
  }
  .author-portrait { position: absolute; left: 142px; top: 248px; }
  .tagline-box {
    position: absolute; left: 13px; top: 750px; width: 547px; height: 66px;
    border: 1.5px solid var(--rule); display: flex; align-items: center; justify-content: center;
    font-family: "Roboto", sans-serif; font-weight: 900; font-size: 23px;
    font-variant: small-caps; letter-spacing: 0.6px; color: var(--white);
  }
  .tagline-number { font-size: 30px; font-style: italic; margin-right: 8px; }
  .author-band {
    position: absolute; left: 0; top: 831px; width: 100%; height: 62px;
    border-top: 1.5px solid #777; border-bottom: 1.5px solid #777;
    display: flex; align-items: center; justify-content: center;
    font-family: "Roboto", sans-serif; font-weight: 900; font-size: 33px;
    letter-spacing: 0.5px; color: var(--gold);
  }
</style>
</head>
<body>
<main class="cover">
  <section class="back-cover">
    <div class="excerpt-box">
      <p class="excerpt-text">“As years have gone by I have become much more conscious about my problem with stuttering, more able to relax my muscles to alleviate it. At the age of 20, I realized that stuttering is like a demon in my head that needs to be killed and that nothing is wrong with me. Furthermore, no one can help me but myself. I’m holding the key of my future. Everything is just in my head.</p>
      <p class="excerpt-text">With this book, I want to help you realize that nobody can help you fix your stuttering better than yourself. There’s no quick-get-rid-of-stuttering cure. The cure lies inside of you.”</p>
      <p class="excerpt-credit">—Lukas Orbeck, excerpt from Chapter One</p>
    </div>
    <div class="about-box">
      <h2 class="about-title">ABOUT THE AUTHOR</h2>
    </div>
    <div class="isbn-box">
      <p class="isbn-label">ISBN-Barcode</p>
    </div>
  </section>

  <section class="spine">
    <span class="spine-title">BEYOND THE SILENT PAUSE</span>
    <span class="spine-author">LUKAS ORBECK</span>
  </section>

  <section class="front-cover">
    <h1 class="book-title">BEYOND THE<br>SILENT PAUSE</h1>
    <p class="book-subtitle">My Story</p>
    <svg class="author-portrait" width="292" height="466" viewBox="0 0 292 466" role="img" aria-label="Portrait photograph of the author">
      <defs>
        <radialGradient id="portraitTone" cx="50%" cy="42%" r="60%">
          <stop offset="0%" stop-color="#8a7466"/>
          <stop offset="55%" stop-color="#3d3733"/>
          <stop offset="100%" stop-color="#141414"/>
        </radialGradient>
      </defs>
      <ellipse cx="146" cy="233" rx="145" ry="232" fill="url(#portraitTone)"/>
    </svg>
    <div class="tagline-box"><span class="tagline-number">5</span>Steps to Speaking Fluently Forever</div>
    <div class="author-band">LUKAS ORBECK</div>
  </section>
</main>
</body>
</html>
```